Vertical retractable banner/pop-up for conference

We need a banner for a personal tax business based in Luxembourg to use at conferences/presentations etc.

The company name is Brevin Tax & Consulting - please view the website www.brevintax.example for the style of our business and use of colours.

The colours we use are:-
#7D1935
#4A96AD
#F5F3EE

Also uploaded are the logo files and the template from the printing company to ensure that the sizes/margins are correct.

Requirements
Must have
• Use of corporate colours (see above).
• Logo
• Website address
Nice to have
• We are open to ideas on style so do not want to prescribe too much as we would like to receive a variety of possible designs ranging from the more minimalist options to more detailed. Some considerations for the design could be to use:-
• 1) The tagline from the website - "Specialists in personal and expatriate taxation".
• 2) The website background is a picture of Luxembourg - if similar city pictures are used on the banner then they should be of Luxembourg also (i.e. not other cities).

```html
<!DOCTYPE html>
<html lang="en">
<head>
<meta charset="utf-8">
<title>Brevin Tax &amp; Consulting – Banner Revision 2</title>
<link rel="stylesheet" href="https://fonts.googleapis.com/css2?family=Mulish:wght@400&family=Roboto+Condensed:wght@300&family=Raleway:wght@300&family=Roboto:wght@300&display=swap">
<style>
  :root {
    --maroon: #660040;
    --maroon-deep: #3a0024;
    --maroon-soft: #b0588c;
    --paper: #ffffff;
    --board-light: #f2f2f2;
    --board-dark: #c4c4c4;
    --city-light: #f4f4f4;
    --city-mid: #cfcfcf;
    --city-dark: #a9a9a9;
    --label: #ececec;
  }
  html, body {
    margin: 0;
    padding: 0;
    width: 1200px;
    height: 781px;
    overflow: hidden;
    background: var(--board-light);
  }
  .presentation-board {
    display: block;
    width: 1200px;
    height: 781px;
  }
  .revision-label {
    font-family: "Roboto", Arial, sans-serif;
    font-weight: 300;
    font-size: 82px;
    fill: var(--label);
  }
  .brand-name, .brand-sub {
    font-family: "Mulish", "Helvetica Neue", sans-serif;
    font-weight: 400;
    fill: var(--maroon);
  }
  .tagline {
    font-family: "Roboto Condensed", "Arial Narrow", sans-serif;
    font-weight: 300;
  }
  .tagline--light { fill: var(--paper); }
  .tagline--dark { fill: var(--maroon); }
  .web-address {
    font-family: "Raleway", "Helvetica Neue", sans-serif;
    font-weight: 300;
    fill: var(--paper);
  }
  .web-address--vertical {
    fill: var(--paper);
    stroke: rgba(120, 120, 120, 0.35);
    stroke-width: 0.6px;
  }
  .band { fill: var(--maroon); }
  .band-highlight { fill: var(--maroon-soft); }
  .brand-dot { fill: none; stroke: var(--maroon); stroke-width: 3; }
</style>
</head>
<body>
<svg class="presentation-board" viewBox="0 0 1200 781" xmlns="http://www.w3.org/2000/svg">
  <defs>
    <linearGradient id="board-fill" x1="0" y1="0" x2="1" y2="0.3">
      <stop offset="0" stop-color="var(--board-dark)"/>
      <stop offset="0.55" stop-color="var(--board-light)"/>
      <stop offset="1" stop-color="#ffffff"/>
    </linearGradient>
    <linearGradient id="city-fill" x1="0" y1="0" x2="0" y2="1">
      <stop offset="0" stop-color="var(--city-light)"/>
      <stop offset="0.45" stop-color="var(--city-mid)"/>
      <stop offset="1" stop-color="var(--city-dark)"/>
    </linearGradient>
    <linearGradient id="base-fill" x1="1" y1="0" x2="0" y2="1">
      <stop offset="0.35" stop-color="var(--maroon)"/>
      <stop offset="1" stop-color="var(--maroon-deep)"/>
    </linearGradient>
  </defs>

  <rect class="board-background" x="0" y="0" width="1200" height="781" fill="url(#board-fill)"/>
  <text class="revision-label" transform="translate(106,600) rotate(-90)">Revision 2</text>

  <!-- Banner A: straight bands -->
  <g class="banner banner--straight">
    <rect x="141" y="42" width="301" height="707" fill="var(--paper)"/>
    <rect class="banner-photo" x="141" y="240" width="301" height="306" fill="url(#city-fill)" role="img" aria-label="Black and white view of Luxembourg old town above the fortress walls"/>
    <rect class="band" x="141" y="42" width="301" height="32"/>
    <rect x="141" y="546" width="301" height="203" fill="url(#base-fill)"/>
    <circle class="brand-dot" cx="205" cy="230" r="36"/>
    <text class="brand-name" x="258" y="242" font-size="40">BREVIN</text>
    <text class="brand-sub" x="259" y="262" font-size="16">TAX &amp; CONSULTING</text>
    <g class="tagline tagline--light" font-size="16" text-anchor="middle">
      <text x="294" y="602">Specialists in</text>
      <text x="294" y="627">Luxembourg, UK and US Personal Tax</text>
      <text x="294" y="652">Compliance and Consulting</text>
    </g>
    <text class="web-address" x="156" y="718" font-size="25" textLength="280" lengthAdjust="spacing">www.brevintax.example</text>
  </g>

  <!-- Banner B: wave bands, centred brand -->
  <g class="banner banner--wave">
    <rect x="512" y="42" width="301" height="707" fill="var(--paper)"/>
    <rect class="banner-photo" x="512" y="250" width="301" height="320" fill="url(#city-fill)" role="img" aria-label="Black and white view of Luxembourg old town above the fortress walls"/>
    <path class="band-highlight" d="M512,82 C620,88 720,62 813,66 V74 C720,72 620,98 512,91 Z"/>
    <path class="band" d="M512,42 H813 V66 C720,62 620,88 512,82 Z"/>
    <path class="band-highlight" d="M512,477 C610,466 700,548 813,540 V560 H512 Z"/>
    <path class="band" d="M512,484 C610,474 700,560 813,552 V749 H512 Z"/>
    <circle class="brand-dot" cx="657" cy="195" r="55"/>
    <text class="brand-name" x="662" y="316" font-size="48" text-anchor="middle">BREVIN</text>
    <text class="brand-sub" x="662" y="339" font-size="19" text-anchor="middle">TAX &amp; CONSULTING</text>
    <g class="tagline tagline--light">
      <text x="541" y="586" font-size="15">Specialists in</text>
      <text x="541" y="612" font-size="23">Luxembourg, UK and US</text>
      <text x="543" y="633" font-size="15">Personal Tax Compliance and Consulting</text>
    </g>
    <text class="web-address" x="522" y="722" font-size="26" textLength="280" lengthAdjust="spacing">www.brevintax.example</text>
  </g>

  <!-- Banner C: wave bands, vertical web address -->
  <g class="banner banner--vertical-url">
    <rect x="871" y="42" width="301" height="707" fill="var(--paper)"/>
    <rect class="banner-photo" x="871" y="250" width="301" height="300" fill="url(#city-fill)" role="img" aria-label="Black and white view of Luxembourg old town above the fortress walls"/>
    <path class="band-highlight" d="M871,82 C980,88 1080,62 1172,66 V74 C1080,72 980,98 871,91 Z"/>
    <path class="band" d="M871,42 H1172 V66 C1080,62 980,88 871,82 Z"/>
    <path class="band-highlight" d="M871,474 C970,464 1060,540 1172,532 V550 H871 Z"/>
    <path class="band" d="M871,481 C970,472 1060,552 1172,544 V749 H871 Z"/>
    <circle class="brand-dot" cx="1020" cy="205" r="55"/>
    <text class="brand-name" x="1027" y="318" font-size="48" text-anchor="middle">BREVIN</text>
    <text class="brand-sub" x="1027" y="344" font-size="19" text-anchor="middle">TAX &amp; CONSULTING</text>
    <g class="tagline tagline--dark">
      <text x="938" y="428" font-size="13">Specialists in</text>
      <text x="938" y="451" font-size="21">Luxembourg, UK and US</text>
      <text x="940" y="470" font-size="13">Personal Tax Compliance and Consulting</text>
    </g>
    <text class="web-address web-address--vertical" transform="translate(882,112) rotate(90)" font-size="40" textLength="590" lengthAdjust="spacing">www.brevintax.example</text>
  </g>
</svg>
</body>
</html>
```